Etiketten-Design für Getränkedose
Zielgruppe
Ich werde Getränke in Dosen 250 ml herstellen lassen, welches ich im Markt vertreiben möchte.
Aufgabenstellung
Das Pfandlogo und die EAN müssen an die Etiketten rangebracht werden, deshalb ist es wichtig, dass wenn Sie keine Möglichkeit haben die EAN ranzubringen, dass Platz im Design frei gehalten wird.
Im Anhang 1 finden Sie die Abmessungen von den Etiketten die an die Dosen rangebracht werden sollen!
Das Design muss innerhalb von diesen Abmessungen erstellt werden.
Es handelt sich hier nur um eine Druckvorlage!
Für so eine Druckvorlage muss auf den Etiketten Platz frei gehalten werden.
Ich benötige von Ihnen 3D Dosendesigns, sowie in meiner Skizze.
Wichtig: Es sollen auschließlich die Farben Weiß und Grün genutzt werden.
Meine Marke heißt ' Silver Plum' und es ist wichtig, dass die Farbe grün mit der Limette von meinem Logo passt.
Anhang 2&3= Mein Logo
Anhang 4= Eine Skizze von mir.
Ganz oben am Dosenrand soll das Wort Plum in Grün NICHT mit eingeführt werden.
Ganz unten soll bitte in Farbe Grau die Zahl: (2018) auf Römisch hinzugefügt werden und das Grau und die Schrift soll bitte mit meinem Logo passen:
MMXVIII
Wichtig: Es soll ein edles und modernes Design werden!
Ich freue mich auf Ihre kreativen Designs.
Als Vorgabe: Die Dose soll weiß sein und es sollen grüne Farben benutzt werden und es soll mit dem Logo farblich übereinstimmen.
Vielen Dank im Voraus

```html
<!DOCTYPE html>
<html lang="de">
<head>
<meta charset="utf-8">
<title>Silver Plum – Dosenetikett</title>
<link rel="stylesheet" href="https://fonts.googleapis.com/css2?family=Montserrat:wght@400&display=swap">
<style>
  :root {
    --label-white: #ffffff;
    --mist-white: #f3f6f1;
    --leaf-pale: #d6e8c8;
    --leaf-mid: #9cc77e;
    --leaf-deep: #5c9a3f;
    --brand-ink: #3a3d3f;
    --year-grey: #6f7472;
    --page: #ffffff;
  }

  html, body {
    margin: 0;
    padding: 0;
    width: 878px;
    height: 1200px;
    overflow: hidden;
    background: var(--page);
  }

  .can-label {
    position: relative;
    width: 878px;
    height: 1200px;
    overflow: hidden;
    background:
      linear-gradient(to bottom,
        var(--label-white) 0%,
        var(--mist-white) 35%,
        var(--leaf-pale) 60%,
        var(--leaf-mid) 82%,
        var(--leaf-deep) 100%);
  }

  .label-streaks {
    position: absolute;
    inset: 0;
    background: repeating-linear-gradient(to right,
      rgba(255,255,255,0) 0px,
      rgba(255,255,255,0.22) 30px,
      rgba(255,255,255,0) 70px,
      rgba(120,170,90,0.06) 110px,
      rgba(255,255,255,0) 150px);
  }

  .ornament-field {
    position: absolute;
    left: 120px;
    top: 120px;
    width: 640px;
    height: 620px;
    border-radius: 50%;
    background: radial-gradient(ellipse at center,
      rgba(190,215,170,0.35) 0%,
      rgba(220,235,208,0.18) 50%,
      rgba(255,255,255,0) 75%);
  }

  .brand-name {
    position: absolute;
    left: 0;
    right: 0;
    top: 430px;
    margin: 0;
    text-align: center;
    font-family: "Montserrat", sans-serif;
    font-weight: 400;
    font-size: 64px;
    line-height: 1;
    letter-spacing: 6px;
    color: var(--brand-ink);
  }

  .vintage-year {
    position: absolute;
    left: 0;
    right: 0;
    bottom: 62px;
    margin: 0;
    text-align: center;
    font-family: "Montserrat", sans-serif;
    font-weight: 400;
    font-size: 22px;
    letter-spacing: 6px;
    color: var(--year-grey);
  }
</style>
</head>
<body>
  <main class="can-label">
    <div class="label-streaks"></div>
    <div class="ornament-field" role="img" aria-label="Zartes florales Rankenornament in hellem Grün hinter dem Markennamen"></div>

    <h1 class="brand-name">SILVER PLUM</h1>

    <p class="vintage-year">MMXVIII</p>
  </main>
</body>
</html>
```